Merchant Discount Program Needs a Business Card Design

We are in need of a business card design for a new start-up based in Northern Virginia called "Brightmark" (a play on words of "24/7"). We are creating a vast merchant network featuring varying services and industries to offer to our subscribers/members. Our initial tangible product will be a "Brightmark VIP" card that members would provide at the physical location of participating merchants (merchants will display a decal on window or signage near cash register/POS system). We would like to see business card designs that uses a vibrant orange color. The design should have a "hometown" feel as we really are looking to foster loyalty with our members and great local merchants in their communities.
Business
We are interested in seeing designs that look like a credit card or member card on the front (orange background and logo image in white). The back will include the contact info. We are also interested in seeing single-sided examples as well.
- Calibri or TW Cen MT

```html
<!DOCTYPE html>
<html lang="en">
<head>
<meta charset="utf-8">
<title>Brightmark Business Card</title>
<link rel="stylesheet" href="https://fonts.googleapis.com/css2?family=Carlito:wght@400;700&display=swap">
<style>
  :root {
    --orange: #f29a1f;
    --black: #0d0d0d;
    --white: #ffffff;
    --ground: #e9e6e1;
    --ink: #1a1a1a;
  }
  * { margin: 0; padding: 0; box-sizing: border-box; }
  html, body { width: 1200px; height: 892px; overflow: hidden; }
  body {
    background: var(--ground);
    font-family: "Carlito", "Calibri", sans-serif;
    position: relative;
  }
  .card {
    position: absolute;
    left: 250px;
    width: 700px;
    height: 400px;
    overflow: hidden;
    border-radius: 6px;
    box-shadow: 0 6px 18px rgba(0,0,0,.18);
  }
  .card--front { top: 26px; }
  .card--back { top: 466px; }
  .card__shapes { position: absolute; inset: 0; width: 100%; height: 100%; }

  .brand__name { position: absolute; color: var(--orange); font-weight: 700; line-height: 1; letter-spacing: -1px; }
  .brand__tagline { position: absolute; color: var(--orange); font-weight: 400; }

  /* front */
  .card--front .brand__name { left: 70px; top: 100px; font-size: 92px; }
  .card--front .brand__tagline { left: 76px; top: 206px; font-size: 20px; }
  .front__web {
    position: absolute; right: 34px; bottom: 24px;
    font-size: 34px; color: var(--ink); font-weight: 400; line-height: 1;
  }

  /* back */
  .holder { position: absolute; left: 34px; top: 40px; color: var(--ink); }
  .holder__name { font-size: 34px; font-weight: 700; line-height: 1; }
  .holder__role { font-size: 17px; margin-top: 6px; }
  .card--back .brand__name { right: 34px; top: 60px; font-size: 56px; }
  .card--back .brand__tagline { right: 36px; top: 124px; font-size: 14px; }
  .contact {
    position: absolute; right: 34px; top: 190px;
    list-style: none; color: var(--orange); font-size: 22px; line-height: 1;
  }
  .contact__item { display: flex; justify-content: flex-end; align-items: center; gap: 14px; margin-bottom: 12px; }
  .contact__icon { width: 24px; height: 24px; flex: none; }
</style>
</head>
<body>

<section class="card card--front" aria-label="Card front">
  <svg class="card__shapes" viewBox="0 0 700 400" preserveAspectRatio="none" aria-hidden="true">
    <rect width="700" height="400" fill="var(--orange)"/>
    <path d="M0 0 H700 V176 Q420 352 0 386 Z" fill="var(--white)"/>
    <path d="M0 0 H700 V150 Q410 330 0 372 Z" fill="var(--black)"/>
  </svg>
  <p class="brand__name">Brightmark</p>
  <p class="brand__tagline">Local savings for every neighbor.</p>
  <p class="front__web">www.brightmarkvip.com</p>
</section>

<section class="card card--back" aria-label="Card back">
  <svg class="card__shapes" viewBox="0 0 700 400" preserveAspectRatio="none" aria-hidden="true">
    <rect width="700" height="400" fill="var(--orange)"/>
    <path d="M330 0 H700 V400 H250 Q250 120 330 0 Z" fill="var(--white)"/>
    <path d="M400 0 H700 V400 H272 Q282 118 400 0 Z" fill="var(--black)"/>
  </svg>
  <div class="holder">
    <p class="holder__name">Employee name</p>
    <p class="holder__role">Managing Director</p>
  </div>
  <p class="brand__name">Brightmark</p>
  <p class="brand__tagline">Local savings for every neighbor.</p>
  <ul class="contact">
    <li class="contact__item">555-0142 0188
      <svg class="contact__icon" viewBox="0 0 24 24" aria-hidden="true"><rect width="24" height="24" rx="3" fill="var(--orange)"/><path d="M8 5 L10 5 L11 9 L9.5 10 Q11 13.5 14 14.5 L15 13 L19 14 L19 16 Q18 19 15 18.5 Q7 16 5.5 8 Q5.5 5.5 8 5 Z" fill="var(--black)"/></svg>
    </li>
    <li class="contact__item">hello@brightmarkvip.com
      <svg class="contact__icon" viewBox="0 0 24 24" aria-hidden="true"><rect width="24" height="24" rx="3" fill="var(--orange)"/><rect x="5" y="7" width="14" height="10" fill="var(--black)"/><path d="M5 7 L12 13 L19 7" stroke="var(--orange)" stroke-width="1.5" fill="none"/></svg>
    </li>
    <li class="contact__item">www.brightmarkvip.com
      <svg class="contact__icon" viewBox="0 0 24 24" aria-hidden="true"><rect width="24" height="24" rx="3" fill="var(--orange)"/><circle cx="12" cy="12" r="6.5" fill="none" stroke="var(--black)" stroke-width="2"/><path d="M5.5 12 H18.5 M12 5.5 V18.5" stroke="var(--black)" stroke-width="1.5"/></svg>
    </li>
    <li class="contact__item">120 Harbor Lane Suite 2
      <svg class="contact__icon" viewBox="0 0 24 24" aria-hidden="true"><rect width="24" height="24" rx="3" fill="var(--orange)"/><path d="M12 19 Q6 12 6 10 A6 6 0 0 1 18 10 Q18 12 12 19 Z" fill="var(--black)"/><circle cx="12" cy="10" r="2" fill="var(--orange)"/></svg>
    </li>
    <li class="contact__item">Maplecrest, VA 00000<span class="contact__icon" aria-hidden="true"></span></li>
  </ul>
</section>

</body>
</html>
```